Healthcare technology company website - Quorin

Create wireframe design for Quorin, an Australian based medical technology company developing a robotic ultrasound system.

Current site quorin.com
https://www.plansketch.example/proto/k7LmP2xQ9rTzW4bN8cV1Ya/Quorin-Website?node-id=2210-4471&t=hRtP3wQzLmN8kXvB-1.
https://www.plansketch.example/proto/k7LmP2xQ9rTzW4bN8cV1Ya/Quorin-Website?page-id=2207%3A518&node-id=2238-3302&viewport=-33%2C513%2C0.15&t=MfK2sLrQpZ7dNwY4-1&scaling=min-zoom&content-scaling=fixed&starting-point-node-id=2238%3A3302
The attached mp4 to be the hero view. Open to designer who can improve it. Attached figma

Industry/Entity Type

tech healthcare

Number of Pages Required

4 page

Requirements
Must have
• Hero view with mp4 attached. Hardware interaction model similar to https://www.lumetra.example/au/sonibuds-4/ div class="section section-redesigned no-pad-bottom will-change"

```html
<!DOCTYPE html>
<html lang="en">
<head>
<meta charset="utf-8">
<title>Quorin — Vascular Imaging, Reimagined</title>
<link href="https://fonts.googleapis.com/css2?family=Roboto:wght@100;300;400;500;700;900&display=swap" rel="stylesheet">
<style>
:root{
  --ink:#1f1f24;
  --muted:#555a66;
  --pink:#c8215d;
  --purple:#9a5bd6;
  --violet:#7b3fe4;
  --blush:#fbeef2;
  --blush-deep:#f4dde6;
  --lavender:#f3ecfa;
  --lavender-deep:#e6d9f2;
  --footer:#2b1a4b;
  --footer-line:#43326a;
  --white:#ffffff;
  --field-line:#cfcfd6;
  --ghost:rgba(40,20,60,0.045);
}
*{margin:0;padding:0;box-sizing:border-box}
html,body{width:1200px;height:3488px;overflow:hidden}
body{font-family:'Roboto',sans-serif;color:var(--ink);background:var(--white);position:relative}
.abs{position:absolute}
.pill-btn{position:absolute;display:flex;align-items:center;justify-content:center;border-radius:40px;border:3px solid transparent;
  background:linear-gradient(var(--white),var(--white)) padding-box,linear-gradient(90deg,var(--pink),var(--purple)) border-box;
  color:var(--pink);font-weight:500;text-transform:uppercase;letter-spacing:.2px}

/* nav */
.site-nav{left:145px;top:51px;width:910px;height:84px;border-radius:42px;background:var(--white);box-shadow:0 6px 24px rgba(0,0,0,.08)}
.nav-brand{position:absolute;left:52px;top:18px;font-size:40px;font-weight:300;letter-spacing:1px;color:var(--ink)}
.nav-link{position:absolute;top:33px;font-size:15px;font-weight:500;color:var(--ink)}
.nav-link.active::after{content:"";position:absolute;left:0;right:0;bottom:-9px;height:3px;border-radius:2px;background:linear-gradient(90deg,var(--pink),var(--purple))}
.nav-cta{left:758px;top:21px;width:126px;height:43px;font-size:14px}

/* hero */
.hero-wordmark{left:0;width:1200px;top:175px;text-align:center;font-size:210px;font-weight:300;letter-spacing:6px;color:var(--ink);line-height:1}
.play-btn{left:552px;top:266px;width:96px;height:96px}
.hero-tagline{left:0;width:1200px;top:428px;text-align:center;font-size:62px;font-weight:700;
  background:linear-gradient(90deg,#9b33c9,#7b3fe4);-webkit-background-clip:text;background-clip:text;color:transparent}

/* mission */
.mission-band{left:0;top:555px;width:1200px;height:819px}
.ghost-word{position:absolute;left:0;width:1200px;text-align:center;font-weight:900;color:var(--ghost);line-height:1;letter-spacing:4px}
.mission-copy{left:0;width:1200px;top:724px;text-align:center;font-size:24px;font-weight:300;line-height:41px;color:#333}
.mission-copy strong{display:block;font-size:30px;font-weight:500;color:var(--pink);line-height:44px}
.mission-btn{left:519px;top:875px;width:162px;height:54px;font-size:17px}
.divider{left:145px;top:983px;width:910px;height:1px;background:#e2cdd6}
.section-title{position:absolute;left:0;width:1200px;text-align:center;font-size:50px;font-weight:400;color:var(--ink)}
.partner{position:absolute;width:144px;height:144px;border-radius:50%;background:#f9f5f7;box-shadow:0 4px 16px rgba(120,60,90,.08);display:flex;align-items:center;justify-content:center}
.partner.focus{background:var(--white);border:3px solid var(--purple);width:148px;height:148px}
.partner-badge{width:86px;height:30px;border-radius:6px;background:#d9cdd4}

/* products */
.product-heading{position:absolute;font-size:28px;font-weight:500;color:var(--ink)}
.product-copy{position:absolute;font-size:15.5px;line-height:28px;color:var(--muted);text-align:justify}
.product-btn{width:142px;height:50px;font-size:16px}
.hw-ring{left:149px;top:1570px;width:434px;height:434px;border-radius:50%;background:var(--white);box-shadow:0 10px 40px rgba(0,0,0,.08)}
.hw-photo{left:183px;top:1604px;width:366px;height:366px;border-radius:50%;background:linear-gradient(180deg,#e9e9ee 0%,#dcdce6 40%,#6f6ad8 75%,#4b46b8 100%)}
.sw-ring{left:765px;top:2061px;width:352px;height:352px;border-radius:50%;border:8px solid #e2e5e4}
.monitor{left:645px;top:2115px;width:406px;height:238px;background:#111;border-radius:4px;padding:6px}
.monitor-screen{width:100%;height:100%;background:linear-gradient(90deg,#f3f3f3 0 28%,#dcdcdc 28% 100%)}
.monitor-neck{left:823px;top:2353px;width:50px;height:34px;background:linear-gradient(#cfcfcf,#eee)}
.monitor-foot{left:763px;top:2385px;width:170px;height:14px;border-radius:4px;background:linear-gradient(#e8e8e8,#c9c9c9)}

/* contact */
.contact-band{left:0;top:2498px;width:1200px;height:677px}
.field{position:absolute;background:var(--white);border:1px solid var(--field-line);font-size:16px;color:#555;padding:0 22px;display:flex;align-items:center}
.field.msg{align-items:flex-start;padding-top:16px}
.submit-btn{left:528px;top:3026px;width:142px;height:48px;font-size:16px}

/* footer */
.site-footer{left:0;top:3175px;width:1200px;height:313px;background:var(--footer);color:var(--white)}
.info-icon{position:absolute;width:44px;height:44px;border-radius:50%;border:1.5px solid rgba(255,255,255,.7);display:flex;align-items:center;justify-content:center}
.info-icon.accent{background:var(--pink);border:none}
.info-text{position:absolute;font-size:15px;line-height:24px}
.footer-link{position:absolute;top:163px;font-size:16px;font-weight:500;text-transform:uppercase}
.footer-rule{position:absolute;left:0;top:244px;width:1200px;height:1px;background:var(--footer-line)}
.copyright{position:absolute;left:145px;top:262px;font-size:13px;color:#e6e0f0}
.social{position:absolute;top:257px;width:29px;height:29px;border-radius:50%;border:1.5px solid rgba(255,255,255,.8)}
</style>
</head>
<body>

<!-- navigation -->
<nav class="abs site-nav">
  <div class="nav-brand">quorin</div>
  <span class="nav-link active" style="left:390px">ABOUT</span>
  <span class="nav-link" style="left:478px">TECHNOLOGY</span>
  <span class="nav-link" style="left:613px">WORK WITH US</span>
  <span class="pill-btn nav-cta">Get in touch</span>
</nav>

<!-- hero -->
<header>
  <div class="abs hero-wordmark">quorin</div>
  <svg class="abs play-btn" viewBox="0 0 96 96" role="img" aria-label="Play hero video">
    <circle cx="48" cy="48" r="48" fill="#e33a35"/>
    <path d="M38 28 L70 48 L38 68 Z" fill="#f7c9c3"/>
  </svg>
  <h1 class="abs hero-tagline">Vascular Imaging, Reimagined</h1>
</header>

<!-- mission & partners -->
<section>
  <svg class="abs mission-band" viewBox="0 0 1200 819" preserveAspectRatio="none" aria-hidden="true">
    <defs>
      <linearGradient id="blush" x1="0" y1="0" x2="0" y2="1">
        <stop offset="0" stop-color="#fdf4f7"/><stop offset="1" stop-color="#f4dde6"/>
      </linearGradient>
      <linearGradient id="pinkline" x1="0" x2="1">
        <stop offset="0" stop-color="#c8215d" stop-opacity=".2"/><stop offset=".3" stop-color="#c8215d"/><stop offset="1" stop-color="#c8215d" stop-opacity=".1"/>
      </linearGradient>
    </defs>
    <path d="M0 68 C200 110 330 115 420 90 C560 40 700 0 960 0 L1200 0 L1200 819 L0 819 Z" fill="url(#blush)"/>
    <path d="M230 113 C420 120 470 70 620 30 C740 0 860 -5 960 6" fill="none" stroke="url(#pinkline)" stroke-width="2.5"/>
  </svg>
  <div class="ghost-word" style="top:688px;font-size:285px">Mission</div>
  <p class="abs mission-copy">Quorin is a Medical Imaging,Deep Learning and Robotics Company<br>on a mission to improve lives by Developing the next generation of<strong>Vascular Imaging Solutions</strong></p>
  <span class="pill-btn mission-btn">Learn more</span>
  <div class="abs divider"></div>
  <h2 class="section-title" style="top:1016px">Our Partners</h2>
  <div class="partner" style="left:142px;top:1148px"><span class="partner-badge"></span></div>
  <div class="partner" style="left:296px;top:1109px"><span class="partner-badge"></span></div>
  <div class="partner focus" style="left:449px;top:1146px"><span class="partner-badge"></span></div>
  <div class="partner" style="left:605px;top:1109px"><span class="partner-badge"></span></div>
  <div class="partner" style="left:759px;top:1148px"><span class="partner-badge"></span></div>
  <div class="partner" style="left:914px;top:1109px"><span class="partner-badge"></span></div>
</section>

<!-- products -->
<section>
  <div class="ghost-word" style="top:1376px;font-size:270px">Products</div>
  <h2 class="section-title" style="top:1466px">Our Products</h2>

  <div class="abs hw-ring"></div>
  <div class="abs hw-photo" role="img" aria-label="Robotic ultrasound scanning bed with a patient's arm resting in the blue scanning channel"></div>
  <h3 class="product-heading" style="left:619px;top:1622px">HARDWARE</h3>
  <p class="product-copy" style="left:619px;top:1676px;width:438px">Nemo enim ipsam voluptatem quia voluptas sit aspernatur aut odit aut fugit, sed quia consequuntur magni dolores eos qui ratione voluptatem sequi nesciuneque porro quisquam est, qui dolorem ipsum quia dolor sit amet, consectetur, adipisci velit, sed quia non numquam eius modi tempora incidunt ut labore et dolore magnam aliquam quaerat voluptatem enim ad minima vis nostrum et dolore magnam aliquam quaerat voluptatem enim.</p>
  <span class="pill-btn product-btn" style="left:619px;top:1896px">Learn more</span>

  <h3 class="product-heading" style="left:145px;top:2095px">SOFTWARE</h3>
  <p class="product-copy" style="left:145px;top:2148px;width:406px">Nemo enim ipsam voluptatem quia voluptas sit aspernatur aut odit aut fugit, sed quia consequuntur magni dolores eos qui ratione voluptatem sequi nesciuneque porro quisquam est, qui dolorem ipsum quia dolor sit amet, consectetur, adipisci velit, sed quia non numquam eius modi tempora incidunt ut labore et dolore magnam aliquam quaerat voluptatem enim ad minima vis nostrum et dolore magnam</p>
  <span class="pill-btn product-btn" style="left:145px;top:2369px">Learn more</span>

  <div class="abs sw-ring"></div>
  <div class="abs monitor"><div class="monitor-screen" role="img" aria-label="Imaging software dashboard showing a 3D vessel model and waveform charts"></div></div>
  <div class="abs monitor-neck"></div>
  <div class="abs monitor-foot"></div>
</section>

<!-- contact -->
<section>
  <svg class="abs contact-band" viewBox="0 0 1200 677" preserveAspectRatio="none" aria-hidden="true">
    <defs>
      <linearGradient id="lav" x1="0" y1="0" x2="0" y2="1">
        <stop offset="0" stop-color="#faf7fd"/><stop offset="1" stop-color="#e8dcf3"/>
      </linearGradient>
      <linearGradient id="purpleline" x1="0" x2="1">
        <stop offset="0" stop-color="#9a5bd6" stop-opacity=".1"/><stop offset=".45" stop-color="#9a5bd6"/><stop offset="1" stop-color="#9a5bd6" stop-opacity=".1"/>
      </linearGradient>
    </defs>
    <path d="M0 68 C120 20 260 0 400 10 C560 25 680 100 840 112 C980 122 1100 95 1200 70 L1200 677 L0 677 Z" fill="url(#lav)"/>
    <path d="M220 2 C420 0 540 50 640 88 C740 122 860 118 980 110" fill="none" stroke="url(#purpleline)" stroke-width="2.5"/>
  </svg>
  <div class="ghost-word" style="top:2960px;font-size:280px;color:rgba(60,20,90,.05)">Contact</div>
  <h2 class="section-title" style="top:2652px">Contact Us</h2>
  <div class="field" style="left:233px;top:2750px;width:361px;height:54px">First Name</div>
  <div class="field" style="left:604px;top:2750px;width:361px;height:54px">Last Name</div>
  <div class="field" style="left:233px;top:2815px;width:361px;height:54px">Email address</div>
  <div class="field" style="left:604px;top:2815px;width:361px;height:54px">Phone Number</div>
  <div class="field msg" style="left:233px;top:2880px;width:732px;height:115px">Message</div>
  <span class="pill-btn submit-btn">Submit</span>
</section>

<!-- footer -->
<footer class="abs site-footer">
  <div class="info-icon" style="left:227px;top:63px">
    <svg width="14" height="18" viewBox="0 0 14 18" aria-hidden="true"><path d="M7 0C3.1 0 0 3 0 6.8 0 11.9 7 18 7 18s7-6.1 7-11.2C14 3 10.9 0 7 0z" fill="#fff"/><circle cx="7" cy="6.8" r="2.4" fill="#2b1a4b"/></svg>
  </div>
  <p class="info-text" style="left:289px;top:61px">314,At vero eos et accu<br>samus et iusto odio dimos ducimu</p>
  <div class="info-icon accent" style="left:569px;top:63px">
    <svg width="18" height="18" viewBox="0 0 24 24" aria-hidden="true"><path d="M6.6 10.8a15.1 15.1 0 0 0 6.6 6.6l2.2-2.2c.3-.3.7-.4 1-.2 1.1.4 2.3.6 3.6.6.6 0 1 .4 1 1V20c0 .6-.4 1-1 1A17 17 0 0 1 3 4c0-.6.4-1 1-1h3.5c.6 0 1 .4 1 1 0 1.3.2 2.5.6 3.6.1.3 0 .7-.2 1z" fill="#fff"/></svg>
  </div>
  <p class="info-text" style="left:631px;top:73px;font-weight:500;font-size:16px">+1 888 888 8888</p>
  <div class="info-icon" style="left:801px;top:63px">
    <svg width="18" height="14" viewBox="0 0 18 14" aria-hidden="true"><rect width="18" height="14" rx="2" fill="#fff"/><path d="M1 1.5 9 7.5 17 1.5" fill="none" stroke="#2b1a4b" stroke-width="1.6"/></svg>
  </div>
  <p class="info-text" style="left:864px;top:72px">info@quorin.com</p>

  <span class="footer-link" style="left:299px">Home</span>
  <span class="footer-link" style="left:391px">About</span>
  <span class="footer-link" style="left:489px">Technology</span>
  <span class="footer-link" style="left:639px">Work with us</span>
  <span class="footer-link" style="left:802px">Contact us</span>

  <div class="footer-rule"></div>
  <p class="copyright">Copyrights © 2025 Quorin.All rights reserved &nbsp;|&nbsp; Privacy Policy &nbsp;|&nbsp; Terms of Use</p>
  <span class="social" style="left:920px" aria-label="Social link"></span>
  <span class="social" style="left:956px;background:#fff" aria-label="Social link"></span>
  <span class="social" style="left:992px" aria-label="Social link"></span>
  <span class="social" style="left:1028px" aria-label="Social link"></span>
</footer>

</body>
</html>
```